Landscaping flier 2024

Create a 1 page flier for landscaping services
1. Must be completed in Adobe Photoshop
2. Size 8.5" x 11" (portrait layout)
3. Include logo
4. Text to include:
2024 Gravesite Landscaping Packages
info@maplecrestmemorial.example
(201) 555-0148
maplecrestmemorial.example
5. Use chart text for the content. DO NOT COPY THE CHART DESIGN/FORMAT. Use the chart for the text you need only.
6. Use "Pricing cards as format for laying out the chart". Open to other ideas as well.
**Use the example of chart design (handwritten) to base your design off of.
7. Photos
-include before and after care photos

```html
<!DOCTYPE html>
<html lang="en">
<head>
<meta charset="UTF-8">
<title>Maplecrest Memorial – 2024 Gravesite Landscaping Packages</title>
<link href="https://fonts.googleapis.com/css2?family=Quicksand:wght@400;500;600&display=swap" rel="stylesheet">
<style>
  :root {
    --maroon: #7d1f2d;
    --white: #ffffff;
    --stage: #e9e6e6;
    --photo-sky: #9fa79c;
    --photo-stone: #b7bab6;
    --photo-grass: #6fa83f;
    --photo-grass-dry: #8f9a5a;
  }
  * { margin: 0; padding: 0; box-sizing: border-box; }
  html, body { width: 1200px; height: 1200px; overflow: hidden; }
  body {
    background: var(--stage);
    font-family: "Quicksand", sans-serif;
    position: relative;
  }
  .flyer {
    position: absolute;
    left: 172px; top: 46px;
    width: 857px; height: 1106px;
    background: var(--maroon);
    overflow: hidden;
    box-shadow: 0 6px 24px rgba(0,0,0,0.25);
  }
  .masthead {
    position: absolute; left: 0; top: 0;
    width: 100%; height: 204px;
    background: var(--white);
    display: flex; flex-direction: column; align-items: center; justify-content: center; gap: 12px;
  }
  .brand {
    display: flex; align-items: center; gap: 18px;
  }
  .brand-mark {
    width: 22px; height: 22px; border-radius: 50%;
    background: var(--maroon);
  }
  .brand-name {
    color: var(--maroon);
    font-weight: 600;
    font-size: 40px;
    letter-spacing: 1px;
  }
  .headline {
    color: var(--maroon);
    font-weight: 500;
    font-size: 20px;
    letter-spacing: 2px;
    text-transform: uppercase;
  }
  .care-photos {
    position: absolute; left: 0; top: 204px;
    width: 100%; height: 397px;
    display: flex; gap: 4px;
    background: var(--white);
  }
  .care-photo { flex: 1; height: 100%; }
  .photo-before {
    background: linear-gradient(180deg, var(--photo-sky) 0%, var(--photo-stone) 35%, var(--photo-stone) 58%, var(--photo-grass-dry) 78%, #7a844a 100%);
  }
  .photo-after {
    background: linear-gradient(180deg, var(--photo-sky) 0%, var(--photo-stone) 35%, var(--photo-stone) 58%, var(--photo-grass) 78%, #5e9435 100%);
  }
  .package-frame { position: absolute; left: 0; top: 0; }
  .package-col { position: absolute; top: 0; height: 100%; }
  .col-seasonal { left: 74px; --ink: var(--white); }
  .col-basic { left: 334px; --ink: var(--maroon); }
  .col-endowment { left: 594px; --ink: var(--white); }
  .package-title, .package-lead, .feature {
    position: absolute; left: 26px; width: 214px;
    color: var(--ink);
    font-size: 16px; font-weight: 500; line-height: 20px;
  }
  .package-title { color: var(--maroon); top: 639px; }
  .feature svg {
    position: absolute; left: -26px; top: 2px;
    width: 16px; height: 16px;
    stroke: var(--ink); stroke-width: 2.6; fill: none; stroke-linecap: round; stroke-linejoin: round;
  }
  .contact-line {
    position: absolute; left: 0; top: 1047px; width: 100%;
    text-align: center;
    color: var(--white);
    font-size: 16px; font-weight: 500;
  }
</style>
</head>
<body>
<main class="flyer">
  <header class="masthead">
    <div class="brand">
      <span class="brand-mark"></span>
      <span class="brand-name">Maplecrest Memorial</span>
    </div>
    <h1 class="headline">2024 Gravesite Landscaping Packages</h1>
  </header>

  <div class="care-photos">
    <div class="care-photo photo-before" role="img" aria-label="Before care: family headstones with overgrown, untrimmed shrubs and patchy lawn"></div>
    <div class="care-photo photo-after" role="img" aria-label="After care: granite family headstones with neatly trimmed boxwood shrubs on green lawn"></div>
  </div>

  <svg class="package-frame" width="857" height="1106" viewBox="0 0 857 1106" aria-hidden="true">
    <path fill="#ffffff" d="M59,624 H797 A12,12 0 0 1 809,636 V661 A12,12 0 0 1 797,673 H571 A10,10 0 0 0 561,683 V1006 A18,18 0 0 1 543,1024 H312 A18,18 0 0 1 294,1006 V683 A10,10 0 0 0 284,673 H59 A12,12 0 0 1 47,661 V636 A12,12 0 0 1 59,624 Z"/>
  </svg>

  <section class="package-col col-seasonal">
    <h2 class="package-title">Seasonal Care</h2>
    <p class="package-lead" style="top:680px">Seasonal Landscaping<br>care</p>
    <p class="feature" style="top:740px"><svg viewBox="0 0 16 16"><path d="M2 8.5 L6 12.5 L14 3.5"/></svg>Wedding trimme</p>
    <p class="feature" style="top:780px"><svg viewBox="0 0 16 16"><path d="M3 3 L13 13 M13 3 L3 13"/></svg>Movement leveling</p>
    <p class="feature" style="top:820px"><svg viewBox="0 0 16 16"><path d="M3 3 L13 13 M13 3 L3 13"/></svg>Payment gave<br>care forever</p>
    <p class="feature" style="top:880px"><svg viewBox="0 0 16 16"><path d="M3 3 L13 13 M13 3 L3 13"/></svg>Full bed of<br>boxwood shape</p>
    <p class="feature" style="top:940px"><svg viewBox="0 0 16 16"><path d="M3 3 L13 13 M13 3 L3 13"/></svg>Replacement of shape</p>
    <p class="feature" style="top:980px"><svg viewBox="0 0 16 16"><path d="M3 3 L13 13 M13 3 L3 13"/></svg>Trust Certificate</p>
  </section>

  <section class="package-col col-basic">
    <h2 class="package-title">Basic Care Endourment</h2>
    <p class="package-lead" style="top:680px">Landscaping care<br>with no planting</p>
    <p class="feature" style="top:740px"><svg viewBox="0 0 16 16"><path d="M2 8.5 L6 12.5 L14 3.5"/></svg>Wedding &amp; Trimming</p>
    <p class="feature" style="top:780px"><svg viewBox="0 0 16 16"><path d="M2 8.5 L6 12.5 L14 3.5"/></svg>Movement leveling</p>
    <p class="feature" style="top:820px"><svg viewBox="0 0 16 16"><path d="M2 8.5 L6 12.5 L14 3.5"/></svg>Payment ensure<br>grave care forever</p>
    <p class="feature" style="top:880px"><svg viewBox="0 0 16 16"><path d="M3 3 L13 13 M13 3 L3 13"/></svg>Full bed of<br>boxwood shape</p>
    <p class="feature" style="top:940px"><svg viewBox="0 0 16 16"><path d="M3 3 L13 13 M13 3 L3 13"/></svg>Replacement of shape</p>
    <p class="feature" style="top:980px"><svg viewBox="0 0 16 16"><path d="M3 3 L13 13 M13 3 L3 13"/></svg>Trust Certificate</p>
  </section>

  <section class="package-col col-endowment">
    <h2 class="package-title">Basic Care Endourment</h2>
    <p class="package-lead" style="top:680px">Landscaping care with<br>no planting</p>
    <p class="feature" style="top:740px"><svg viewBox="0 0 16 16"><path d="M2 8.5 L6 12.5 L14 3.5"/></svg>Wedding &amp; Trimming</p>
    <p class="feature" style="top:780px"><svg viewBox="0 0 16 16"><path d="M2 8.5 L6 12.5 L14 3.5"/></svg>Movement leveling</p>
    <p class="feature" style="top:820px"><svg viewBox="0 0 16 16"><path d="M2 8.5 L6 12.5 L14 3.5"/></svg>Payment ensure<br>grave care forever</p>
    <p class="feature" style="top:880px"><svg viewBox="0 0 16 16"><path d="M2 8.5 L6 12.5 L14 3.5"/></svg>Full bed of<br>boxwood shape</p>
    <p class="feature" style="top:940px"><svg viewBox="0 0 16 16"><path d="M2 8.5 L6 12.5 L14 3.5"/></svg>Replacement of shape</p>
    <p class="feature" style="top:980px"><svg viewBox="0 0 16 16"><path d="M2 8.5 L6 12.5 L14 3.5"/></svg>Trust Certificate</p>
  </section>

  <footer class="contact-line">(201) 555-0148 | info@maplecrestmemorial.example | maplecrestmemorial.example</footer>
</main>
</body>
</html>
```